Events Company Needs Website Revamp

Harbor Showcases is an events company that specializes in organizing and marketing large scale consumer and trade events globally.

The new web design should provide easy classification of the events, and allow visitors to find and access the details page within 2 clicks.

There are no strict guidelines on the color theme. It just has to blend naturally with the corporate logo.
Updates

The company logo is uploaded (pdf & ai)

I came across this design which I like very much. Elegant and corporate with nice modern fonttype.

Layout wise, neat and clear. 

Please see how you can emulate the design further. Particularly, highlighting the 2 event arms (Trade/Consumer) clearly.

Target Market(s)

Consumer looking for upcoming events, B2C companies looking to participate, B2B companies looking to connect with other companies

Industry/Entity Type

It Company

Requirements
Must have
• The new design should help to achieve the following objectives:
1) Visitors should be able to easily identify and access the 2 different types of events (i.e. Trade Events and Consumer Events).
2) Visitors should be able to easily find events that interest them (e.g. filter by date, trade or consumer, category [i.e. beauty, retail, F&B, construction, etc.]).
3) Visitors should be able to access an event’s details page within 2 clicks from any page.

Main navigation to include the following links:
- About Us
- Calendar
- Consumer Events
- Trade Events
- Contact Us

Design for Three (3) pages required:
A. Homepage
- Clear differentiation and easy access to the 2 different types of events (trade and consumer)
- Featured area to showcase latest 4-5 events
- Quick way to access events calendar
- Clear call-to-action for newsletter signup
- Social media sharing widgets/buttons
- A section for latest news and press releases
- A section for featured testimonials

B. Events Listing Page
- List of links to all events
- Logos and/or photos of events
- Filter / tags to find events in a specific category (e.g. food, electronics, building & construction, etc.)

C. Events Details Page
- Photo strip to showcase event photos / brochure
- A section with event details (Date, Venue, Event Description, etc.)
- Call-to-action button to visit event website
- Call-to-action button to contact event sales team
- E.g. http://vemlo.com/user/launchgrovehq/launch-weekend-2011 but with the photo strip permanently extended and of a shorter height. Event details and call-to-action buttons should also be easily seen

```html
<!DOCTYPE html>
<html lang="en">
<head>
<meta charset="utf-8">
<title>Harbor Showcases – Trade &amp; Consumer Events</title>
<link rel="stylesheet" href="https://fonts.googleapis.com/css2?family=Oswald:wght@400;500&family=Poiret+One&family=Roboto:ital,wght@0,400;0,700;1,400&display=swap">
<style>
:root{
  --orange:#e8622c;
  --orange-light:#f07a3a;
  --red:#d9341f;
  --nav-dark:#c9301c;
  --purple:#5a1466;
  --purple-dark:#3d0b47;
  --ink:#1c1c1c;
  --text:#7a7a7a;
  --muted:#9a9a9a;
  --line:#e4e4e4;
  --rule:#e2e2e2;
  --white:#ffffff;
}
*{box-sizing:border-box;margin:0;padding:0}
html,body{width:900px;height:1200px;overflow:hidden;background:var(--white)}
body{position:relative;font-family:"Roboto",Arial,sans-serif;color:var(--text)}
.abs{position:absolute}

/* header */
.site-header{position:absolute;left:0;top:0;width:900px;height:140px;
  background:radial-gradient(ellipse 420px 140px at 460px 90px,#f07c3c 0%,#e9582a 55%,#dd3f24 100%)}
.site-header::after{content:"";position:absolute;left:0;right:0;bottom:-4px;height:8px;
  background:radial-gradient(ellipse 420px 6px at 450px 0,#7a2a6e 0%,rgba(122,42,110,.4) 60%,transparent 100%)}
.brand{position:absolute;left:38px;top:-55px;width:150px;height:135px;border-radius:50%;
  background:var(--white);border:3px solid var(--orange-light);box-shadow:0 2px 6px rgba(0,0,0,.25)}
.brand-name{position:absolute;left:0;right:0;top:82px;text-align:center;font:500 13px "Oswald",sans-serif;color:var(--ink);letter-spacing:.3px}
.brand-name::before{content:"";display:inline-block;width:9px;height:9px;border-radius:50%;background:var(--orange);margin-right:5px;vertical-align:0}

.main-nav{position:absolute;left:314px;top:0;height:54px;display:flex;font:500 19px "Oswald",sans-serif;color:var(--white)}
.main-nav a{display:block;padding-top:21px;height:54px;color:inherit;text-decoration:none;text-align:center;border-left:1px solid rgba(255,255,255,.18);white-space:nowrap}
.main-nav a.current{background:var(--nav-dark);border-left:none}
.sub-nav{position:absolute;left:314px;top:54px;width:298px;height:33px;background:var(--nav-dark);
  font:12px "Roboto",sans-serif;color:var(--white)}
.sub-nav span{position:absolute;top:9px}
.sub-nav i{position:absolute;top:9px;width:1px;height:15px;background:rgba(255,255,255,.35)}

/* event arms */
.arm-title{font:39px "Poiret One",sans-serif;color:var(--ink);white-space:nowrap}
.arm-text{font-size:12px;line-height:19px;color:var(--text);width:262px}
.btn-more{width:88px;height:31px;border:1px solid #cfcfcf;background:linear-gradient(#fdfdfd,#e9e9e9);
  font:500 12px "Oswald",sans-serif;color:var(--red);text-align:center;line-height:29px;box-shadow:0 1px 2px rgba(0,0,0,.12)}
.divider{height:2px;background:var(--rule)}
.globe{left:322px;top:165px;width:268px;height:262px;border-radius:50%;
  background:radial-gradient(circle at 40% 35%,#fafafa 0%,#dcdcdc 55%,#a8a8a8 100%)}
.globe-shadow{left:360px;top:405px;width:190px;height:26px;border-radius:50%;
  background:radial-gradient(ellipse,rgba(0,0,0,.25),transparent 70%)}

/* carousel */
.carousel{left:87px;top:450px;width:724px;height:151px;background:var(--white);border:1px solid #e2e2e2;
  box-shadow:0 10px 16px -8px rgba(0,0,0,.25)}
.car-arrow{top:487px;width:36px;height:70px;background:linear-gradient(#f3f3f3,#d9d9d9)}
.car-arrow.prev{left:56px;border-radius:36px 0 0 36px}
.car-arrow.next{left:806px;border-radius:0 36px 36px 0}
.card{background:var(--white);border:1px solid #dadada}
.card .photo{position:absolute;background:linear-gradient(#6a6c70,#2d2a27 70%,#1a1612)}
.card .photo.mic{background:linear-gradient(#eeeeee,#c8c8c8 60%,#9c9c9c)}
.card .cap{position:absolute;font:700 11px "Poiret One",sans-serif;color:var(--red)}

/* lower sections */
.sec-title{font:28px "Poiret One",sans-serif;color:var(--ink);white-space:nowrap}
.news-badge{width:44px;height:42px;border:1px solid #e2e2e2;background:var(--white)}
.news-badge span{position:absolute;left:7px;top:9px;width:30px;height:24px;background:#f2a33a;border-radius:3px}
.news-title{font:500 15px "Oswald",sans-serif;color:#6a6a6a}
.news-text,.quote-text{font-size:12px;line-height:19.5px;color:var(--text)}
.read-more{font-size:12.5px;color:var(--red)}
.quote-mark{font:700 40px "Oswald",sans-serif;color:#8a8a8a;line-height:1}
.author{font:italic 12px "Roboto",sans-serif;color:var(--ink);text-align:right}

/* calendar */
.calendar{left:631px;top:707px;width:230px;height:228px;background:var(--white);border:1px solid #dcdcdc;
  box-shadow:0 8px 14px -6px rgba(0,0,0,.3)}
.cal-head{position:absolute;left:-1px;top:-1px;width:230px;height:36px;background:linear-gradient(90deg,var(--purple-dark),var(--purple) 40%,var(--purple) 80%,var(--purple-dark));
  color:var(--white);font:700 18px "Poiret One",sans-serif;text-align:center;line-height:36px}
.cal-head .nav{position:absolute;top:0;width:24px;height:36px;background:rgba(0,0,0,.25)}
.cal-days{position:absolute;top:43px;left:0;width:228px;display:grid;grid-template-columns:repeat(7,1fr);
  font-size:10.5px;color:#777;text-align:center;letter-spacing:.5px}
.cal-grid{position:absolute;top:63px;left:0;width:228px;display:grid;grid-template-columns:repeat(7,1fr);grid-auto-rows:33px}
.cal-grid span{border-right:1px solid var(--line);border-bottom:1px solid var(--line);
  font-size:15px;color:var(--ink);text-align:center;line-height:32px}
.cal-grid span:nth-child(7n){border-right:none}
.cal-grid span.soft{background:#ececec;color:#777}
.cal-grid span.today{background:var(--red);color:var(--white)}
.cal-tip{left:653px;top:766px;width:118px;height:60px;background:linear-gradient(#f06a30,#dd3c20);color:var(--white);
  box-shadow:0 2px 5px rgba(0,0,0,.3)}
.cal-tip b{position:absolute;left:8px;top:5px;font:700 12px "Poiret One",sans-serif}
.cal-tip p{position:absolute;left:8px;top:22px;width:100px;font:700 8px/10px "Roboto",sans-serif}

/* footer */
.footer-rule{left:0;top:1010px;width:900px;height:8px}
.foot-head{font:500 13px "Oswald",sans-serif;color:var(--ink)}
.foot-text{font-size:11.5px;line-height:13.5px;color:#777}
.social{width:25px;height:25px;border-radius:50%;background:var(--purple-dark)}
.email-field{left:566px;top:1103px;width:157px;height:20px;border:1px solid #cfcfcf;font:italic 11px "Roboto",sans-serif;color:#999;padding:3px 6px}
.email-submit{left:722px;top:1103px;width:49px;height:20px;background:linear-gradient(#fdfdfd,#e3e3e3);border:1px solid #cfcfcf;
  font:700 9px "Roboto",sans-serif;color:var(--purple-dark);text-align:center;line-height:18px}
</style>
</head>
<body>

<header class="site-header">
  <div class="brand"><div class="brand-name">Harbor Showcases</div></div>
  <nav class="main-nav">
    <a class="current" style="width:94px">About Us</a><a style="width:89px">Calendar</a><a style="width:119px">Trade Events</a><a style="width:152px">Consumer Events</a><a style="width:110px">Contact Us</a>
  </nav>
  <div class="sub-nav">
    <i style="left:16px"></i><span style="left:39px">Our&nbsp;&nbsp; Story</span>
    <i style="left:117px"></i><span style="left:143px">History</span>
    <i style="left:202px"></i><span style="left:228px">Missios</span>
    <i style="left:288px"></i>
  </div>
</header>

<!-- event arms -->
<h1 class="abs arm-title" style="left:38px;top:213px">Trade Events</h1>
<p class="abs arm-text" style="left:40px;top:281px">Lorem ipsum dolor sit amet, consectetur adipiscing elit. Curabitur ac lorem eu sem congue pharetra. Vestibulum eget lacus nibh.</p>
<div class="abs btn-more" style="left:38px;top:357px">View More</div>
<div class="abs divider" style="left:38px;top:408px;width:283px"></div>

<h1 class="abs arm-title" style="left:540px;top:213px;width:322px;text-align:right">Consumer Events</h1>
<p class="abs arm-text" style="left:600px;top:281px;text-align:right">Lorem ipsum dolor sit amet, consectetur adipiscing elit. Curabitur ac lorem eu sem congue pharetra. Vestibulum eget lacus nibh.</p>
<div class="abs btn-more" style="left:774px;top:357px">View More</div>
<div class="abs divider" style="left:578px;top:408px;width:282px"></div>

<div class="abs globe-shadow"></div>
<div class="abs globe" role="img" aria-label="Sphere built from white cubes carrying event logos"></div>

<!-- featured events -->
<div class="abs car-arrow prev"><svg width="36" height="70"><path d="M19 26 L11 35 L19 44 Z" fill="#d9341f"/></svg></div>
<div class="abs car-arrow next"><svg width="36" height="70"><path d="M13 26 L21 35 L13 44 Z" fill="#d9341f"/></svg></div>
<div class="abs carousel"></div>

<div class="abs card" style="left:101px;top:471px;width:123px;height:113px">
  <div class="photo" style="left:5px;top:5px;width:111px;height:81px" role="img" aria-label="Speaker on stage in front of an audience"></div>
  <div class="cap" style="left:7px;top:93px">Event Name</div>
</div>
<div class="abs card" style="left:237px;top:471px;width:123px;height:113px">
  <div class="photo" style="left:5px;top:5px;width:111px;height:81px" role="img" aria-label="Speaker on stage in front of an audience"></div>
  <div class="cap" style="left:7px;top:93px">Event Name</div>
</div>
<div class="abs card" style="left:376px;top:457px;width:149px;height:137px">
  <div class="photo mic" style="left:7px;top:6px;width:134px;height:99px" role="img" aria-label="Row of microphones at a press conference"></div>
  <div class="cap" style="left:9px;top:113px;font-size:13px">Event Name</div>
</div>
<div class="abs card" style="left:539px;top:471px;width:123px;height:113px">
  <div class="photo" style="left:5px;top:5px;width:111px;height:81px" role="img" aria-label="Speaker on stage in front of an audience"></div>
  <div class="cap" style="left:7px;top:93px">Event Name</div>
</div>
<div class="abs card" style="left:675px;top:471px;width:123px;height:113px">
  <div class="photo" style="left:5px;top:5px;width:111px;height:81px" role="img" aria-label="Speaker on stage in front of an audience"></div>
  <div class="cap" style="left:7px;top:93px">Event Name</div>
</div>

<div class="abs divider" style="left:38px;top:648px;width:820px"></div>

<!-- latest news -->
<h2 class="abs sec-title" style="left:37px;top:700px">Latest News</h2>
<div class="abs news-badge" style="left:38px;top:757px"><span></span></div>
<h3 class="abs news-title" style="left:93px;top:753px">Lorem Ipsum</h3>
<div class="abs divider" style="left:93px;top:778px;width:205px;height:1px"></div>
<p class="abs news-text" style="left:93px;top:786px;width:215px">Lorem ipsum dolor sit amet, vehicula integer tortor libero, mollis sed...</p>
<a class="abs read-more" style="left:94px;top:830px">Read More</a>

<div class="abs news-badge" style="left:38px;top:868px"><span></span></div>
<h3 class="abs news-title" style="left:93px;top:864px">Lorem Ipsum</h3>
<div class="abs divider" style="left:93px;top:889px;width:205px;height:1px"></div>
<p class="abs news-text" style="left:93px;top:897px;width:215px">Lorem ipsum dolor sit amet, vehicula integer tortor libero, mollis sed...</p>
<a class="abs read-more" style="left:94px;top:941px">Read More</a>

<!-- testimonials -->
<h2 class="abs sec-title" style="left:337px;top:700px">Testimonials</h2>
<div class="abs quote-mark" style="left:338px;top:752px">&ldquo;</div>
<p class="abs quote-text" style="left:369px;top:752px;width:225px">Lorem ipsum dolor sit amet, consectetur adipiscing elit. Curabitur ac lorem eu sem congue pharetra.</p>
<div class="abs author" style="left:369px;top:812px;width:214px">Daniel Marsh</div>
<div class="abs quote-mark" style="left:338px;top:844px">&ldquo;</div>
<p class="abs quote-text" style="left:369px;top:844px;width:225px">Lorem ipsum dolor sit amet, consectetur adipiscing elit. Curabitur ac lorem eu sem congue pharetra.</p>
<div class="abs author" style="left:369px;top:904px;width:214px">Daniel Marsh</div>
<a class="abs read-more" style="left:369px;top:941px">Read More</a>

<!-- calendar -->
<div class="abs calendar">
  <div class="cal-head">
    <span class="nav" style="left:0"><svg width="24" height="36"><path d="M15 11 L9 18 L15 25" stroke="#fff" stroke-width="2.5" fill="none"/></svg></span>
    MAY 2010
    <span class="nav" style="right:0"><svg width="24" height="36"><path d="M9 11 L15 18 L9 25" stroke="#fff" stroke-width="2.5" fill="none"/></svg></span>
  </div>
  <div class="cal-days"><span>SUN</span><span>MON</span><span>TUE</span><span>WED</span><span>THU</span><span>FRI</span><span>SAT</span></div>
  <div class="cal-grid">
    <span></span><span>1</span><span>2</span><span>3</span><span>4</span><span>5</span><span>6</span>
    <span>7</span><span>8</span><span>9</span><span>10</span><span>11</span><span class="soft">12</span><span>13</span>
    <span>14</span><span>15</span><span class="today">16</span><span>17</span><span>18</span><span>19</span><span>20</span>
    <span>21</span><span>22</span><span>23</span><span>24</span><span>25</span><span>26</span><span>27</span>
    <span>28</span><span>29</span><span>30</span><span>31</span><span></span><span></span><span></span>
  </div>
</div>
<div class="abs cal-tip">
  <b>Event Name</b>
  <p>Lorem ipsum dolor sit amet, consectetur.</p>
  <svg class="abs" style="left:106px;top:44px" width="8" height="10"><path d="M2 2 L6 5 L2 8" stroke="#fff" stroke-width="1.3" fill="none"/></svg>
  <svg class="abs" style="left:52px;top:59px" width="16" height="8"><path d="M0 0 L8 8 L16 0 Z" fill="#dd3c20"/></svg>
</div>

<!-- footer -->
<svg class="abs footer-rule" viewBox="0 0 900 8" preserveAspectRatio="none">
  <path d="M0 6 Q450 -4 900 6 Z" fill="#3d0b47"/>
  <rect x="0" y="5.5" width="900" height="2.5" fill="#f07a2a"/>
</svg>

<h4 class="abs foot-head" style="left:39px;top:1062px">Copyright</h4>
<p class="abs foot-text" style="left:39px;top:1084px">© Harbor Showcases 2009-2010. All Rights Reserved.</p>
<p class="abs foot-text" style="left:39px;top:1117px">• Tel: (65) 5550-1840 or (65) 5550-1841<br>• Fax: (65) 5550-1890<br>• hello@harborshowcases.example</p>

<h4 class="abs foot-head" style="left:368px;top:1060px">Connect wit Us</h4>
<div class="abs social" style="left:368px;top:1086px" aria-label="Social network"></div>
<div class="abs social" style="left:401px;top:1086px" aria-label="Social network"></div>
<div class="abs social" style="left:434px;top:1086px" aria-label="News feed"></div>
<div class="abs social" style="left:468px;top:1086px" aria-label="Email">
  <svg width="25" height="25"><rect x="6.5" y="8" width="12" height="9" fill="#fff"/><path d="M6.5 8 L12.5 13 L18.5 8" stroke="#3d0b47" stroke-width="1" fill="none"/></svg>
</div>

<h4 class="abs foot-head" style="left:566px;top:1060px">Subscribe</h4>
<p class="abs foot-text" style="left:566px;top:1081px">Get free event updates &amp; specials!</p>
<div class="abs email-field">Enter Email</div>
<div class="abs email-submit">SUBMIT</div>

<svg class="abs" style="left:819px;top:1108px" width="28" height="44" aria-label="Back to top">
  <path d="M14 1 L27 18 L19 18 L19 42 L9 42 L9 18 L1 18 Z" fill="#f28a1e" stroke="#e06a10" stroke-width="1"/>
</svg>
<div class="abs" style="left:824px;top:1156px;font-size:11px;color:var(--ink)">Top</div>

</body>
</html>
```